Professional window cleaning services business needs a flyer design

We are looking to attract large businesses such as gyms, car dealerships and fast food restaurants.
-Have over 15 years of experience in this business
-We serve customers in Melbourne and all surrounding suburbs
-Specialising in automated periodical services(daily,weekly,monthly, yearly)
-Our current client base consists of major fast food restaurants, car dealerships and residential properties.

Industry/Entity Type

Window Cleaning

Colors
3176b5
fbed22

Requirements
Must have
• Business Details:
• Name: Brisk Window Cleaning
• Phone no:93402657
• website:www.glintora.com.au
• email: admin@glintora.com.au
• mail: PO BOX 2746, Wrenfield Vale, 3184

```html
<!DOCTYPE html>
<html lang="en">
<head>
<meta charset="utf-8">
<title>Brisk Window Cleaning Flyer</title>
<link href="https://fonts.googleapis.com/css2?family=Roboto+Condensed:wght@400;700&family=Arimo:wght@400&display=swap" rel="stylesheet">
<style>
  :root {
    --brand-blue: #3176b5;
    --deep-blue: #1a5c9c;
    --sky-blue: #62b6df;
    --ink-blue: #235fa8;
    --brand-yellow: #fbed22;
    --white: #ffffff;
  }
  * { margin: 0; padding: 0; box-sizing: border-box; }
  html, body { width: 1200px; height: 857px; overflow: hidden; }
  .flyer {
    position: relative;
    width: 1200px;
    height: 857px;
    overflow: hidden;
    background: radial-gradient(ellipse at 40% 55%, var(--sky-blue) 0%, #3f95cd 45%, var(--deep-blue) 100%);
    font-family: 'Roboto Condensed', Arial, sans-serif;
    color: var(--white);
  }
  .lower-band { position: absolute; inset: 0; }
  .brand-name {
    position: absolute; left: 52px; top: 34px;
    font-weight: 700; font-size: 92px; line-height: 1;
    letter-spacing: 12px; color: var(--brand-yellow);
    white-space: nowrap;
  }
  .mascot-art {
    position: absolute; left: 36px; top: 130px; width: 610px; height: 520px;
    border-radius: 48% 40% 30% 30%;
    background: radial-gradient(ellipse at 50% 45%, #f3d6c2 0%, #e7e9ee 40%, rgba(49,118,181,0) 72%);
  }
  .intro {
    position: absolute; right: 53px; top: 32px; width: 540px;
    text-align: right; font-size: 26px; line-height: 34px; letter-spacing: -0.3px;
  }
  .headline {
    position: absolute; left: 560px; top: 220px; width: 592px; text-align: right;
    font-family: 'Arimo', Arial, sans-serif; font-weight: 400; font-size: 52px; letter-spacing: -1px;
    color: var(--brand-yellow); line-height: 1; white-space: nowrap;
  }
  .tagline {
    position: absolute; left: 600px; top: 277px; width: 552px; text-align: center;
    font-family: 'Arimo', Arial, sans-serif; font-size: 20px; letter-spacing: -0.4px;
    white-space: nowrap;
  }
  .contact-box {
    position: absolute; left: 647px; top: 355px; width: 434px; height: 112px;
    background: var(--brand-yellow); text-align: center; color: var(--ink-blue);
    box-shadow: 3px 4px 6px rgba(0,0,0,0.25);
  }
  .contact-box .phone { font-weight: 700; font-size: 66px; line-height: 1; margin-top: 14px; white-space: nowrap; }
  .contact-box .email { font-family: 'Arimo', Arial, sans-serif; font-size: 20px; margin-top: 2px; }
  .services {
    position: absolute; left: 343px; top: 529px; width: 502px; height: 232px;
    border: 7px solid var(--brand-yellow); border-radius: 34px;
    background: linear-gradient(180deg, #2b79b8 0%, #1b5c97 100%);
    padding: 14px 0 0 28px; list-style: none;
  }
  .services li { position: relative; padding-left: 30px; font-size: 23px; line-height: 28px; }
  .services li.alt { font-family: 'Arimo', Arial, sans-serif; font-size: 22px; margin-top: 10px; }
  .services li.alt + li.alt { margin-top: 8px; }
  .services svg { position: absolute; left: 0; top: 6px; width: 20px; height: 18px; }
  .van-photo {
    position: absolute; left: 755px; top: 622px; width: 402px; height: 220px;
    border: 5px solid var(--white); border-radius: 30px;
    background: linear-gradient(180deg, #b9c6cf 0%, #e9d64a 55%, #7b8a6a 100%);
  }
  .footer-bar {
    position: absolute; left: 0; top: 796px; width: 624px; height: 41px;
    background: var(--brand-yellow); border-radius: 0 21px 21px 0;
    color: var(--ink-blue); display: flex; align-items: center; padding-left: 8px; gap: 28px;
    white-space: nowrap;
  }
  .footer-bar .address { font-weight: 700; font-size: 20px; }
  .footer-bar .web { font-size: 25px; }
</style>
</head>
<body>
<main class="flyer">
  <svg class="lower-band" width="1200" height="857" viewBox="0 0 1200 857" aria-hidden="true">
    <polygon points="0,700 1200,455 1200,857 0,857" fill="#3176b5"/>
  </svg>

  <div class="brand-name">BRISK</div>

  <div class="mascot-art" role="img" aria-label="Cartoon window cleaner in cap and overalls holding a squeegee and pointing at the service list"></div>

  <p class="intro">Brisk Services started trading in 1999 with a clear focus on becoming a market leader in the Window Cleaning Industry. Since then we have proudly built the business based on strong ethical standards, focused on customer service.</p>

  <h1 class="headline">Brisk Window Cleaning</h1>
  <p class="tagline">Melbourne's Premier Window Cleaning Company</p>

  <div class="contact-box">
    <div class="phone">CALL 93402657</div>
    <div class="email">admin@glintora.com.au</div>
  </div>

  <ul class="services">
    <li><svg viewBox="0 0 20 18"><path d="M1 10 L7 16 L19 1" fill="none" stroke="#fbed22" stroke-width="4"/></svg>15 years of experience in this business</li>
    <li><svg viewBox="0 0 20 18"><path d="M1 10 L7 16 L19 1" fill="none" stroke="#fbed22" stroke-width="4"/></svg>Specialising in automated periodical services<br>(daily,weekly,monthly, yearly)</li>
    <li class="alt"><svg viewBox="0 0 20 18"><path d="M1 10 L7 16 L19 1" fill="none" stroke="#fbed22" stroke-width="4"/></svg>Residential Window Cleaning</li>
    <li class="alt"><svg viewBox="0 0 20 18"><path d="M1 10 L7 16 L19 1" fill="none" stroke="#fbed22" stroke-width="4"/></svg>Commercial Window Cleaning</li>
    <li class="alt"><svg viewBox="0 0 20 18"><path d="M1 10 L7 16 L19 1" fill="none" stroke="#fbed22" stroke-width="4"/></svg>Real Estate Window Cleaning</li>
  </ul>

  <div class="van-photo" role="img" aria-label="Photo of a yellow company van with a ladder rack and a staff member standing beside it"></div>

  <div class="footer-bar">
    <span class="address">PO BOX 2746, Wrenfield Vale, 3184</span>
    <span class="web">www.glintora.com.au</span>
  </div>
</main>
</body>
</html>
```